Business Cards for Internet Security Company

Awesome designers! This is the opportunity to help design cards for a forward thinking network security company. They use threat information gathered from peer groups to make intelligent decisions on what threats are relevant and which arent. ( not that you need this to do designs, but just so you know where they are coming from. ) :-)

We'd like to see a two side design and the deliverables will be in illustrator 4. The logo is attached and the logo colors are attached in the JPG and I've attached a an eps of the logo and icon

Security

```html
<!DOCTYPE html>
<html lang="en">
<head>
<meta charset="utf-8">
<title>Norvane Business Card</title>
<link rel="stylesheet" href="https://fonts.googleapis.com/css2?family=Belleza&family=Source+Sans+3:wght@400&display=swap">
<style>
  :root {
    --page-bg: #ffffff;
    --brand-deep: #215d7b;
    --brand-frame: #1f5f7e;
    --brand-sky: #3a87c4;
    --label-ink: #231f20;
    --card-white: #ffffff;
  }
  * { margin: 0; padding: 0; box-sizing: border-box; }
  html, body {
    width: 900px;
    height: 1200px;
    overflow: hidden;
    background: var(--page-bg);
  }
  .sheet {
    position: relative;
    width: 900px;
    height: 1200px;
  }
  .side-label {
    position: absolute;
    left: 0;
    width: 100%;
    text-align: center;
    font-family: "Source Sans 3", sans-serif;
    font-size: 72px;
    font-weight: 400;
    color: var(--label-ink);
    line-height: 1;
  }
  .side-label--front { top: 40px; }
  .side-label--back { top: 610px; }

  .card {
    position: absolute;
    left: 76px;
    width: 756px;
    height: 442px;
  }
  .card--front {
    top: 121px;
    background: var(--brand-deep);
  }
  .card--back {
    top: 691px;
    background: var(--card-white);
    border: 17px solid var(--brand-frame);
  }

  .wordmark {
    position: absolute;
    display: flex;
    align-items: center;
  }
  .wordmark__dot {
    border-radius: 50%;
    background: var(--brand-sky);
    flex: none;
  }
  .wordmark__name {
    font-family: "Belleza", sans-serif;
    font-weight: 400;
    line-height: 1;
    white-space: nowrap;
  }

  .card--front .wordmark {
    left: 48px;
    top: 160px;
    gap: 26px;
  }
  .card--front .wordmark__dot { width: 112px; height: 112px; }
  .card--front .wordmark__name {
    font-size: 136px;
    color: var(--card-white);
  }

  .card--back .wordmark {
    left: 39px;
    top: 115px;
    gap: 14px;
  }
  .card--back .wordmark__dot { width: 62px; height: 62px; }
  .card--back .wordmark__name {
    font-size: 72px;
    color: var(--brand-deep);
  }

  .contact {
    position: absolute;
    left: 412px;
    top: 232px;
    list-style: none;
    font-family: "Belleza", sans-serif;
    font-size: 28px;
    line-height: 35px;
    color: var(--brand-sky);
  }
</style>
</head>
<body>
  <main class="sheet">
    <h2 class="side-label side-label--front">Front</h2>
    <section class="card card--front" aria-label="Card front">
      <div class="wordmark">
        <span class="wordmark__dot" aria-hidden="true"></span>
        <span class="wordmark__name">Norvane</span>
      </div>
    </section>

    <h2 class="side-label side-label--back">Back</h2>
    <section class="card card--back" aria-label="Card back">
      <div class="wordmark">
        <span class="wordmark__dot" aria-hidden="true"></span>
        <span class="wordmark__name">Norvane</span>
      </div>
      <ul class="contact">
        <li>John Doe</li>
        <li>johnd@norvane.com</li>
        <li>(xxx) xxx-xxxx</li>
        <li>www.norvane.com</li>
      </ul>
    </section>
  </main>
</body>
</html>
```